Cosmetic retail chain developes private label products. We need package designe for creme soap.

We need package designe for bar creme soap in cardboard package. Benchmark is Plim. The name of our private label for this product is Tirsa.

```html
<!DOCTYPE html>
<html lang="en">
<head>
<meta charset="utf-8">
<title>Tirsa – Handmade Soap Bar Package</title>
<link rel="stylesheet" href="https://fonts.googleapis.com/css2?family=Sacramento&family=Indie+Flower&display=swap">
<style>
  :root {
    --paper: #eef2df;
    --paper-leaf: #e2e9d0;
    --frame-orange: #d9711f;
    --panel-white: #ffffff;
    --brand-peach: #e2a46c;
    --ink: #3b3b38;
    --flower-yellow: rgba(233, 217, 122, 0.75);
    --flower-orange: rgba(237, 169, 76, 0.8);
    --flower-deep: rgba(224, 132, 46, 0.75);
    --flower-blush: rgba(240, 186, 150, 0.6);
    --bee-grey: rgba(120, 120, 114, 0.22);
    --clear: rgba(238, 242, 223, 0);
  }
  * { box-sizing: border-box; margin: 0; padding: 0; }
  html, body {
    width: 1200px;
    height: 800px;
    overflow: hidden;
    background: var(--paper);
  }
  .package {
    position: relative;
    width: 1200px;
    height: 800px;
    overflow: hidden;
  }
  .leaf-pattern {
    position: absolute;
    inset: 0;
    background: radial-gradient(ellipse at 70% 30%, var(--paper-leaf) 0%, var(--paper) 65%);
  }
  .floral-cluster {
    position: absolute;
    left: -120px;
    top: 360px;
    width: 760px;
    height: 560px;
    background:
      radial-gradient(closest-side at 100px 90px, var(--flower-yellow) 0%, var(--clear) 100%) 0 0 / 240px 220px no-repeat,
      radial-gradient(closest-side at 150px 150px, var(--flower-orange) 0%, var(--clear) 100%) 130px 120px / 300px 300px no-repeat,
      radial-gradient(closest-side at 140px 140px, var(--flower-orange) 0%, var(--clear) 100%) 60px 230px / 280px 280px no-repeat,
      radial-gradient(closest-side at 140px 120px, var(--flower-blush) 0%, var(--clear) 100%) 290px 270px / 280px 240px no-repeat,
      radial-gradient(closest-side at 140px 120px, var(--flower-deep) 0%, var(--clear) 100%) 360px 300px / 280px 240px no-repeat,
      radial-gradient(closest-side at 100px 90px, var(--flower-yellow) 0%, var(--clear) 100%) 260px 360px / 200px 180px no-repeat;
  }
  .bee {
    position: absolute;
    background: radial-gradient(closest-side, var(--bee-grey) 0%, rgba(120, 120, 114, 0) 100%);
  }
  .bee--upper { left: 150px; top: 335px; width: 140px; height: 140px; }
  .bee--lower { left: 400px; top: 555px; width: 240px; height: 170px; }
  .label-frame {
    position: absolute;
    left: 264px;
    top: 207px;
    width: 672px;
    height: 386px;
    border: 4px solid var(--frame-orange);
  }
  .label-panel {
    position: absolute;
    left: 305px;
    top: 244px;
    width: 588px;
    height: 313px;
    background: var(--panel-white);
    text-align: center;
  }
  .brand-name {
    position: absolute;
    left: 0; right: 0;
    top: 26px;
    font-family: "Sacramento", cursive;
    font-size: 128px;
    line-height: 1;
    color: var(--brand-peach);
    font-weight: 400;
  }
  .product-line {
    position: absolute;
    left: 0; right: 0;
    top: 186px;
    font-family: "Indie Flower", cursive;
    font-size: 29px;
    letter-spacing: 4px;
    color: var(--ink);
  }
  .divider {
    position: absolute;
    left: 252px;
    top: 242px;
    width: 84px;
    height: 10px;
  }
  .skin-type {
    position: absolute;
    left: 0; right: 0;
    top: 263px;
    font-family: "Indie Flower", cursive;
    font-size: 16px;
    letter-spacing: 1px;
    color: var(--ink);
  }
</style>
</head>
<body>
  <main class="package">
    <div class="leaf-pattern" role="img" aria-label="Faint sage leaf pattern on textured cream paper"></div>
    <div class="floral-cluster" role="img" aria-label="Watercolour flowers in yellow and orange with ink outlines"></div>
    <div class="bee bee--upper" role="img" aria-label="Ink sketch of a bee"></div>
    <div class="bee bee--lower" role="img" aria-label="Ink sketch of a bee in flight"></div>

    <div class="label-frame"></div>
    <section class="label-panel">
      <h1 class="brand-name">Tirsa</h1>
      <p class="product-line">A handmade soap Bar</p>
      <svg class="divider" viewBox="0 0 84 10" role="img" aria-label="Small orange divider">
        <line x1="4" y1="5" x2="80" y2="5" stroke="var(--frame-orange)" stroke-width="1.5"/>
        <circle cx="42" cy="5" r="2.5" fill="var(--frame-orange)"/>
      </svg>
      <p class="skin-type">Normal to dry skin</p>
    </section>
  </main>
</body>
</html>
```